依頼概要
・添付させていただきました資料の内容①~⑥をA4サイズにまとめたい。
・文章の内容はそのまま使っていただいても多少変更しても構わない。
・新規顧客訪問した際に簡単に弊社の内容を伝える為のツールとして作成。
・会社のロゴをどこかに入れてほしい
以上になります。
コールセンターのイメージ写真はイメージが湧けばいいので、報告書の部分や文字の部分の変更はお任せします。
入居率は後日、お伝えいたします(確認中)

第一印象がよかったです。

今回は多数の応募をしていただきありがとうございました。

```html
<!DOCTYPE html>
<html lang="ja">
<head>
<meta charset="utf-8">
<title>オーナー様の悩みを解決します! | ひだまり不動産</title>
<link href="https://fonts.googleapis.com/css2?family=Noto+Sans+JP:wght@400;500;700;900&family=Noto+Serif+JP:wght@700;900&display=swap" rel="stylesheet">
<style>
:root{
  --red:#8e1b22;
  --red-deep:#6e1218;
  --cream:#f6ecd9;
  --beige:#e9d9bb;
  --ink:#2a2a2a;
  --accent:#c7252f;
  --white:#ffffff;
}
*{box-sizing:border-box;margin:0;padding:0}
html,body{width:847px;height:1200px;overflow:hidden;background:#fff}
.flyer{position:relative;width:847px;height:1200px;font-family:"Noto Sans JP",sans-serif;color:var(--ink);overflow:hidden}
.hero{position:absolute;left:0;top:0;width:847px;height:1010px;background:var(--red)}
.headline{position:absolute;left:34px;top:26px;font-family:"Noto Serif JP",serif;font-weight:900;color:var(--white);font-size:66px;line-height:76px;letter-spacing:2px}
.hero-art{position:absolute;left:440px;top:70px;width:380px;height:220px;border-radius:6px;background:linear-gradient(160deg,#a8343a,#5d4a3c 60%,#7d5c40)}
.lead{position:absolute;top:288px;height:36px;background:var(--cream);color:var(--red);font-weight:700;font-size:14px;display:flex;align-items:center;justify-content:center;border-radius:2px}
.lead.left{left:34px;width:374px}
.lead.right{left:438px;width:376px;font-size:13px}
.points{position:absolute;left:36px;top:340px;color:var(--white);font-size:14px;line-height:23px;font-weight:500;width:370px}
.points li{list-style:none}
.points .pair{display:flex;gap:22px}
.flow{position:absolute;left:36px;top:430px;width:370px;height:290px}
.occupancy{position:absolute;left:36px;top:880px;color:var(--white);display:flex;align-items:flex-end}
.occupancy .label{font-size:30px;font-weight:700;margin-right:16px;margin-bottom:18px}
.occupancy .rate{font-family:"Noto Sans JP",sans-serif;font-weight:900;font-size:150px;line-height:120px;color:#f3d9d9}
.occupancy .pct{font-size:80px;font-weight:900;line-height:70px;color:#f3d9d9}
.occupancy .note{position:absolute;right:-40px;bottom:-14px;font-size:9px;color:#f3d9d9;white-space:nowrap}
.menu{position:absolute;left:438px;top:346px;width:376px}
.menu-title{font-size:13px;color:var(--white);font-weight:700;margin-bottom:4px}
.menu table{width:100%;border-collapse:collapse;font-size:13px}
.menu td{height:44px;padding:0 12px;border-bottom:2px solid var(--red)}
.menu td.item{background:var(--beige);width:45%;font-weight:500}
.menu td.value{background:var(--white);font-weight:500}
.footer{position:absolute;left:0;top:1010px;width:847px;height:190px;background:var(--white)}
.brand{position:absolute;left:30px;top:34px;display:flex;flex-direction:column;align-items:flex-start;gap:6px}
.brand .mark{width:44px;height:44px;background:var(--red)}
.brand .name{font-size:24px;font-weight:900;color:var(--red)}
.brand .url{font-size:10px;color:var(--ink)}
.company{position:absolute;left:224px;top:22px;width:380px}
.company .desc{font-size:9.5px;line-height:14px}
.company .corp{font-size:27px;font-weight:900;color:var(--red);margin-top:4px}
.company .addr{font-size:9px}
.company .tel{font-size:34px;font-weight:900;color:var(--red);line-height:40px}
.office-photo{position:absolute;left:612px;top:14px;width:206px;height:128px;background:linear-gradient(180deg,#cfe0ec,#d8d8d2 60%,#8d9286)}
.notice{position:absolute;left:0;bottom:0;width:847px;height:36px;background:var(--red);color:var(--white);font-size:13px;font-weight:700;display:flex;align-items:center;padding-left:20px}
</style>
</head>
<body>
<div class="flyer">
  <section class="hero">
    <h1 class="headline">オーナー様の<br>悩みを<br>解決します!</h1>
    <div class="hero-art" role="img" aria-label="握手するオーナー様と担当者、賃貸マンションのイラスト"></div>

    <div class="lead left">市場の調査・分析を行い募集条件を設定</div>
    <div class="lead right">100社以上の仲介会社様への情報提供・訪問営業</div>

    <ul class="points">
      <li>○24時間365日対応の管理専門コールセンターを設けた入居者様対応</li>
      <li class="pair"><span>○解約防止アップ</span><span>○入居者様の満足度アップ</span></li>
    </ul>

    <svg class="flow" viewBox="0 0 370 290" aria-label="コールセンターを中心とした対応の流れ">
      <defs><marker id="ar" markerWidth="8" markerHeight="8" refX="6" refY="4" orient="auto"><path d="M0 0 L8 4 L0 8z" fill="#fff"/></marker></defs>
      <g font-family="Noto Sans JP, sans-serif" font-size="11" text-anchor="middle" font-weight="700">
        <rect x="10" y="20" width="90" height="34" fill="#f6ecd9"/><text x="55" y="42" fill="#8e1b22">オーナー様</text>
        <rect x="270" y="20" width="90" height="34" fill="#f6ecd9"/><text x="315" y="42" fill="#8e1b22">入居者様</text>
        <rect x="125" y="100" width="120" height="44" fill="#fff"/><text x="185" y="119" fill="#8e1b22">管理専門</text><text x="185" y="135" fill="#8e1b22">コールセンター</text>
        <rect x="10" y="200" width="110" height="34" fill="#f6ecd9"/><text x="65" y="222" fill="#8e1b22">管理担当</text>
        <rect x="250" y="200" width="110" height="34" fill="#f6ecd9"/><text x="305" y="222" fill="#8e1b22">協力業者</text>
      </g>
      <g stroke="#fff" stroke-width="2" fill="none" marker-end="url(#ar)">
        <path d="M100 45 L150 98"/><path d="M270 45 L220 98"/>
        <path d="M150 146 L80 198"/><path d="M220 146 L290 198"/>
        <path d="M120 217 L248 217"/>
      </g>
    </svg>

    <div class="occupancy">
      <span class="label">入居率</span>
      <span class="rate">00</span><span class="pct">%</span>
      <span class="note">※2020年4月現在の管理物件</span>
    </div>

    <div class="menu">
      <div class="menu-title">管理メニュー</div>
      <table>
        <tr><td class="item">管理料</td><td class="value">5%〜</td></tr>
        <tr><td class="item">24時間管理人対応</td><td class="value">250円/戸当たり</td></tr>
        <tr><td class="item">敷金</td><td class="value">オーナー様振り</td></tr>
        <tr><td class="item">募集業務(広告費)</td><td class="value">物件により</td></tr>
        <tr><td class="item">定期清掃</td><td class="value">実費請求</td></tr>
        <tr><td class="item">集金業務</td><td class="value">○</td></tr>
        <tr><td class="item">更新業務</td><td class="value">○</td></tr>
        <tr><td class="item">家賃督促</td><td class="value">○</td></tr>
        <tr><td class="item">退去立ち会い・敷金精算</td><td class="value">○</td></tr>
        <tr><td class="item">水道検針・集費用請求</td><td class="value">実費請求</td></tr>
      </table>
    </div>
  </section>

  <footer class="footer">
    <div class="brand">
      <span class="mark"></span>
      <span class="name">ひだまり不動産</span>
      <span class="url">hidamari-f.example</span>
    </div>
    <div class="company">
      <p class="desc">不動産の売買・賃貸・管理のことなら、地域密着の当社へお気軽にご相談ください。</p>
      <p class="corp">株式会社ひだまり不動産</p>
      <p class="addr">本社 〒000-0000 ひだまり市中央区1丁目2-3</p>
      <p class="tel">TEL012-345-6789</p>
    </div>
    <div class="office-photo" role="img" aria-label="ひだまり不動産の店舗外観写真"></div>
    <div class="notice">【ひだまり不動産コールセンター】を完備しております。管理のご相談お待ちしております。</div>
  </footer>
</div>
</body>
</html>
```